Artistic Poster for a Short Film

I am the Writer/Director of an upcoming short film called "Driftwater" and I need a 20x30 poster for the project screening. The screening is coming up very soon so apologies for the quick turnaround time. Here is a short synopsis:

"Walter is a mysterious man who is lost and disoriented. With the help of Marisol, he searches for items out of an old diary written long ago by a woman named Gloria, despite not understanding exactly why he does so. Marisol helps, but when they are unsuccessful she confronts Walter: Does he know why he restlessly searches for these items? The truth is shocking, and reveals Walter's connections to Marisol, Gloria, and the strange old diary.

The truth is that Walter is actually an old man, and Marisol is his caretaker and granddaughter. His memories, including those of Gloria, his deceased wife, have been destroyed by Dementia. He often wakes believing himself to be at an earlier stage of his life, and therefore meets many of the challenges of life with anger and confusion."

Here is the film's website: http://www.driftwater-film.example
Here is our successful Fundbarrow: http://www.fundbarrow.example/projects/502847719/driftwater-a-short-film

The design should be dark and simple. I'm a fan of the art-prints that this short film used (scroll down to see): http://www.fundbarrow.example/projects/ruthvanderlo/kettle-a-short-film-based-on-the-story-by-omar-quill but I'm also open to other ideas. If you google "alternative movie posters" you'll see what I mean. The poster should be simple, easy to read, and hint at the themes of the film without giving the twist away.

Here is a link to the Fine Cut of the film: https://clipvault.example/48210576 The password is: lanterns72
It is not a completed version but will give you an idea of what the film will look like.

Target Market(s)

The intended audience is an art-film crowd of moviegoers.

Industry/Entity Type

Movie

Requirements
Must have
• The poster must have the typical movie poster text at the bottom. The information that should be included is: First line: COPPER LANTERN STUDIOS presents a film by DANIEL OSTROM "DRIFTWATER" MARCEL BRUNAUD TERRA WOLCOTT
Second line: music by OWEN PRATT director of photography VICTOR L. MORALES edited by SIMON ORR costume designer ROBERTA CLINE
Third line: produced by GAIL TORVALD DANIEL OSTROM written and directed by DANIEL OSTROM

It should have the title of the film "Driftwater" and "A film by Daniel Ostrom" on the poster (in addition to the text at the bottom.

It must be high-quality and printable to a size of 20x30. Ideal resolution is 6060x9090. I only need the high quality printable file, I will do the printing myself.
Should not have
• Bright colors.

```html
<!DOCTYPE html>
<html lang="en">
<head>
<meta charset="utf-8">
<title>Driftwater — Poster</title>
<link rel="stylesheet" href="https://fonts.googleapis.com/css2?family=Parisienne&family=Cormorant+SC:wght@500&family=Oswald:wght@500&display=swap">
<style>
  :root {
    --paper: #fbf3e1;
    --cover-dark: #080d10;
    --cover-mid: #16202a;
    --cover-edge: #2b2a26;
    --title: #f6efe0;
    --credit-ink: #2a241f;
  }
  * { margin: 0; padding: 0; box-sizing: border-box; }
  html, body { width: 921px; height: 1200px; overflow: hidden; background: var(--paper); }
  .poster {
    position: relative;
    width: 921px;
    height: 1200px;
    background: var(--paper);
  }
  .diary-cover {
    position: absolute;
    left: 39px;
    top: 36px;
    width: 853px;
    height: 1011px;
    border-radius: 6px 34px 30px 6px;
    background:
      radial-gradient(ellipse at 50% 45%, var(--cover-mid) 0%, var(--cover-dark) 70%),
      var(--cover-dark);
    box-shadow: inset 0 0 0 3px var(--cover-edge), inset 0 0 40px rgba(0,0,0,.8);
  }
  .title-block {
    position: absolute;
    left: 0;
    right: 0;
    top: 450px;
    text-align: center;
    color: var(--title);
  }
  .film-title {
    font-family: "Parisienne", cursive;
    font-weight: 400;
    font-size: 138px;
    line-height: 1;
    letter-spacing: 1px;
  }
  .film-byline {
    margin-top: 6px;
    font-family: "Cormorant SC", serif;
    font-weight: 500;
    font-size: 22px;
    letter-spacing: 4px;
  }
  .billing-block {
    position: absolute;
    left: 0;
    right: 0;
    top: 1078px;
    text-align: center;
    font-family: "Oswald", sans-serif;
    font-weight: 500;
    color: var(--credit-ink);
    text-transform: uppercase;
  }
  .billing-line {
    display: flex;
    justify-content: center;
    align-items: center;
    gap: 7px;
    font-size: 21px;
    line-height: 1.15;
    margin-bottom: 6px;
    letter-spacing: 0.2px;
  }
  .credit-role {
    display: inline-flex;
    flex-direction: column;
    font-size: 8px;
    line-height: 1;
    text-align: right;
    letter-spacing: 0.3px;
  }
  .credit-role.inline { flex-direction: row; font-size: 9px; align-self: center; }
</style>
</head>
<body>
<main class="poster">
  <div class="diary-cover" role="img" aria-label="Worn dark cloth cover of an old diary, scuffed and faded at the edges"></div>

  <header class="title-block">
    <h1 class="film-title">Driftwater</h1>
    <p class="film-byline">A film by Daniel Ostrom</p>
  </header>

  <footer class="billing-block">
    <p class="billing-line">
      <span>COPPER LANTERN STUDIOS</span>
      <span class="credit-role inline">presents a</span>
      <span>DANIEL OSTROM "DRIFTWATER" MARCEL BRUNAUD TERRA WOLCOTT</span>
    </p>
    <p class="billing-line">
      <span class="credit-role"><span>music</span><span>by</span></span>
      <span>OWEN PRATT</span>
      <span class="credit-role"><span>director of</span><span>photography</span></span>
      <span>VICTOR L. MORALES</span>
      <span class="credit-role"><span>edited</span><span>by</span></span>
      <span>SIMON ORR</span>
      <span class="credit-role"><span>costume</span><span>designer</span></span>
      <span>ROBERTA CLINE</span>
    </p>
    <p class="billing-line">
      <span class="credit-role"><span>executive</span><span>producer</span></span>
      <span>GAIL TORVALD DANIEL OSTROM</span>
      <span class="credit-role"><span>written</span><span>by</span></span>
      <span>DANIEL OSTROM</span>
      <span class="credit-role"><span>directed</span><span>by</span></span>
      <span>DANIEL OSTROM</span>
    </p>
  </footer>
</main>
</body>
</html>
```